Harbinger Cargo needs a business card design.

Design a double-sided business card for new freight business. On the front, would like to see our logo along with the following info:

Malcolm Strathby
CEO/FOUNDER
555-207-4163
malcolmstrathby@harbinger-cargo.example

On the reverse side, we would like to use the graphic image of our logo only without the Harbinger Cargo name.

```html
<!DOCTYPE html>
<html lang="en">
<head>
<meta charset="UTF-8">
<title>Harbinger Cargo — Business Card</title>
<link rel="stylesheet" href="https://fonts.googleapis.com/css2?family=Montserrat:wght@400;500;700;800&display=swap">
<style>
  :root {
    --backdrop: #2c2d30;
    --card: #ffffff;
    --navy: #1f1d5c;
    --red: #b0202a;
    --lavender: #d8d6e3;
    --peach: #f2e1d8;
    --pattern-a: #e4e3e5;
    --pattern-b: #f4f4f5;
  }
  * { box-sizing: border-box; margin: 0; padding: 0; }
  html, body { width: 1200px; height: 900px; overflow: hidden; }
  body {
    background: var(--backdrop);
    font-family: "Montserrat", sans-serif;
    display: flex;
    flex-direction: column;
    align-items: center;
    justify-content: center;
    gap: 48px;
  }
  .card {
    width: 600px;
    height: 343px;
    background: var(--card);
    border-radius: 18px;
    position: relative;
    overflow: hidden;
  }
  /* Reverse side */
  .card-back .brand-pattern {
    position: absolute;
    inset: 0;
    background: linear-gradient(115deg, var(--pattern-a) 0%, var(--pattern-b) 70%, #fafafa 100%);
  }
  .card-back .brand-mark {
    position: absolute;
    left: 414px;
    top: 140px;
    width: 52px;
    height: 52px;
    background: var(--red);
    box-shadow: 0 0 0 10px var(--card);
  }
  /* Front side */
  .brand-decoration {
    position: absolute;
    top: 0;
    right: 0;
    width: 300px;
    height: 250px;
    border-bottom-left-radius: 70px;
    background: linear-gradient(100deg, var(--lavender) 0%, var(--lavender) 30%, var(--peach) 60%, #f8ece6 100%);
  }
  .brand {
    position: absolute;
    top: 48px;
    left: 40px;
    display: flex;
    align-items: center;
    gap: 12px;
  }
  .brand-square {
    width: 18px;
    height: 18px;
    background: var(--red);
  }
  .brand-name {
    font-weight: 800;
    font-size: 24px;
    letter-spacing: 2px;
    text-transform: uppercase;
    color: var(--navy);
  }
  .contact {
    position: absolute;
    left: 40px;
    bottom: 36px;
  }
  .contact-name {
    font-weight: 800;
    font-size: 24px;
    color: var(--navy);
  }
  .contact-title {
    font-weight: 400;
    font-size: 17px;
    color: var(--red);
    margin-top: 2px;
    margin-bottom: 14px;
  }
  .contact-line {
    display: flex;
    align-items: center;
    gap: 10px;
    font-size: 16px;
    font-weight: 500;
    color: var(--navy);
    margin-top: 6px;
  }
  .contact-line svg { width: 18px; height: 18px; flex: none; }
</style>
</head>
<body>
  <section class="card card-back" aria-label="Business card reverse">
    <div class="brand-pattern" role="img" aria-label="Repeating brand mark pattern in light grey"></div>
    <div class="brand-mark" role="img" aria-label="Harbinger Cargo brand mark in navy and red"></div>
  </section>

  <section class="card card-front" aria-label="Business card front">
    <div class="brand-decoration" role="img" aria-label="Large faint brand mark decoration in lavender and peach"></div>
    <div class="brand">
      <span class="brand-square"></span>
      <span class="brand-name">Harbinger Cargo</span>
    </div>
    <div class="contact">
      <p class="contact-name">Malcolm Strathby</p>
      <p class="contact-title">CEO/FOUNDER</p>
      <p class="contact-line">
        <svg viewBox="0 0 24 24" aria-hidden="true"><path fill="#b0202a" d="M6.6 10.8a15.1 15.1 0 0 0 6.6 6.6l2.2-2.2c.3-.3.7-.4 1-.2 1.1.4 2.3.6 3.6.6.6 0 1 .4 1 1V20c0 .6-.4 1-1 1A17 17 0 0 1 3 4c0-.6.4-1 1-1h3.5c.6 0 1 .4 1 1 0 1.3.2 2.5.6 3.6.1.3 0 .7-.2 1L6.6 10.8z"/></svg>
        555-207-4163
      </p>
      <p class="contact-line">
        <svg viewBox="0 0 24 24" aria-hidden="true"><path fill="#b0202a" d="M3 5h18c.6 0 1 .4 1 1v12c0 .6-.4 1-1 1H3c-.6 0-1-.4-1-1V6c0-.6.4-1 1-1zm9 7.5L20 7H4l8 5.5z"/></svg>
        malcolmstrathby@harbinger-cargo.example
      </p>
    </div>
  </section>
</body>
</html>
```